Brisk Yard, LLC Web Design

I would like a web site design for a new lawn care business I am creating for my son. This is what it looks like now.

http://www.briskyardllc.example

Target Market(s)

Target customer is blue collar or middle class people who do not have time to do all of the grunt work around their home such as mowing the lawn, clearing snow etc. Or they need help moving or moving something such as mulch or wood. Shoot for an economical audience that may not have thought about having these tasks done for them.

Industry/Entity Type

Lawn Care

Colors
acd037
9bcb3c
cadf82
eaf2cf

Requirements
Must have
• I put in greens below. The colors that were available were not the best greens or the greens I would think about. The greens on the web site are more close.
Nice to have
• Will have a few more pictures of the logo guy on different machines. Will upload as soon as I get.

```html
<!DOCTYPE html>
<html lang="en">
<head>
<meta charset="utf-8">
<title>Brisk Yard, LLC</title>
<link rel="stylesheet" href="https://fonts.googleapis.com/css2?family=Roboto:ital,wght@0,300;0,400;0,500;1,400&display=swap">
<style>
:root{
  --green:#9bcb3c;
  --green-mid:#acd037;
  --green-light:#cadf82;
  --green-pale:#eaf2cf;
  --green-dark:#7fae25;
  --ink:#3a3a3a;
  --muted:#666;
  --footer:#4a4a4a;
  --panel:#e6e6e6;
}
*{box-sizing:border-box;margin:0;padding:0}
html,body{width:1026px;height:1200px;overflow:hidden}
body{font-family:'Roboto',sans-serif;background:#fff;color:var(--ink);position:relative}
.abs{position:absolute}

.header{left:0;top:0;width:1026px;height:97px;background:#fff}
.phone{left:94px;top:37px;display:flex;align-items:center;gap:8px;font-size:15px;color:#555}
.brand{left:0;width:1026px;top:33px;text-align:center;font-size:24px;font-weight:500;color:#3d8a1c}
.brand span{display:inline-block;width:14px;height:14px;border-radius:50%;background:var(--green);margin-right:8px;vertical-align:middle}
.social-top{left:838px;top:35px;display:flex;gap:3px}
.social-top i{display:block;width:30px;height:28px;border-radius:3px}

.hero{left:0;top:97px;width:1026px;height:489px;background:linear-gradient(180deg,#3f95d8 0%,#7fbde9 38%,#9fcf5a 48%,#6fae2c 70%,#5c9c23 100%)}
.nav{left:94px;top:97px;width:838px;height:59px;background:linear-gradient(180deg,#a8d23c,#8dc22e);border:1px solid #c8e483;border-top:none;border-radius:0 0 3px 3px;display:flex;align-items:center;justify-content:space-between;padding:0 36px 0 22px}
.nav a{color:#fff;text-decoration:none;font-size:14px;letter-spacing:.2px}
.nav a.active{background:var(--green-pale);color:#444;padding:9px 14px;border-radius:3px;border:1px solid #fff}
.slide{left:91px;top:222px;width:837px;height:270px;background:#fff;border:2px solid #fff;box-shadow:0 2px 6px rgba(0,0,0,.25);overflow:hidden}
.slide-photo{position:absolute;inset:0;background:linear-gradient(120deg,#3b4a2a 0%,#6d7d3a 35%,#c9e64a 55%,#596b34 80%,#2e3826 100%);clip-path:polygon(212px 0,100% 0,100% 100%,337px 100%,297px 190px)}
.slide-title{position:absolute;left:0;top:32px;width:240px;height:47px;background:var(--green-pale);clip-path:polygon(0 0,213px 0,240px 47px,0 47px);font-size:20px;color:#555;padding:12px 0 0 12px;letter-spacing:.3px}
.slide-text{position:absolute;left:20px;top:96px;width:220px;font-size:10.5px;line-height:18px;color:#555;font-weight:300;text-align:justify}
.slide-btn{position:absolute;left:177px;top:189px;width:152px;height:45px;background:var(--green);clip-path:polygon(0 0,130px 0,152px 45px,0 45px);color:#fff;font-size:14px;font-weight:500;padding:15px 0 0 29px}
.arrow{width:36px;height:41px;background:rgba(40,60,30,.75);display:flex;align-items:center;justify-content:center}

.features{left:0;top:586px;width:1026px;height:115px;background:var(--green)}
.feature-box{width:105px;height:95px;background:#fff;text-align:center;font-size:14px;line-height:15px;color:#222;padding-top:8px}
.feature-box svg{display:block;margin:0 auto 6px}
.feature-title{font-size:17px;color:#fff;letter-spacing:.3px}
.feature-text{font-size:9.5px;line-height:14.5px;color:#fff;text-transform:uppercase;width:290px}

h2.section{font-size:15px;font-weight:400;color:#333;letter-spacing:.2px}
.welcome-img{left:94px;top:766px;width:227px;height:149px;background:linear-gradient(160deg,#8fc24a,#5e9a2a 60%,#4a7f1e)}
.welcome-text{left:340px;top:767px;width:323px;font-size:10.5px;line-height:17.1px;color:#555;text-align:justify}
.read-more{left:340px;top:896px;font-size:11px;font-style:italic;color:var(--green-dark)}
.cta{left:95px;top:939px;width:570px;height:59px;background:linear-gradient(180deg,#a8d23c,#8dc22e);border-radius:2px;color:#fff;font-size:19px;padding:17px 0 0 37px;box-shadow:0 1px 2px rgba(0,0,0,.2)}

.contact-panel{left:691px;top:757px;width:239px;height:242px;background:linear-gradient(180deg,#f2f2f2,var(--panel))}
.field{left:709px;width:202px;height:34px;background:#fff;border:1px solid #ddd;font-size:10px;color:#999;padding:11px 0 0 8px;letter-spacing:.3px}
.submit{left:710px;top:958px;width:92px;height:27px;background:var(--green);border:1px solid #cfe79a;border-radius:2px;color:#fff;font-size:13px;text-align:center;padding-top:6px}

.footer{left:0;top:1051px;width:1026px;height:149px;background:var(--footer)}
.footer-links{left:94px;top:1093px;width:594px;display:flex;align-items:center;font-size:11px;color:#ddd}
.footer-links span.sep{display:inline-block;width:1px;height:28px;background:#888;transform:rotate(25deg);margin:0 17px}
.footer-line{left:94px;top:1126px;width:594px;height:1px;background:#5e5e5e}
.footer-social{left:748px;top:1091px;display:flex;gap:22px}
.footer-social i{display:block;width:19px;height:19px;border-radius:50%;background:#f2f2f2}
.copyright{left:0;width:1026px;top:1157px;text-align:center;font-size:11px;color:#bbb}
</style>
</head>
<body>

<header class="abs header"></header>
<div class="abs phone">
  <svg width="17" height="17" viewBox="0 0 17 17"><rect width="17" height="17" rx="3" fill="#3aa935"/><path d="M5 4c.6-.4 1.1-.3 1.4.2l.8 1.4c.2.4.1.8-.2 1.1l-.6.5c.5 1.1 1.4 2 2.5 2.5l.5-.6c.3-.3.7-.4 1.1-.2l1.4.8c.5.3.6.8.2 1.4-.7 1-1.8 1.2-3 .7C7 11 5.9 9.9 5.2 8 4.7 6.8 4.1 5 5 4z" fill="#fff"/></svg>
  555-014-2200
</div>
<div class="abs brand"><span></span>Brisk Yard, LLC</div>
<div class="abs social-top">
  <i style="background:#4fb3e8"></i><i style="background:#3b5ea6"></i><i style="background:#3a3a3a"></i>
</div>

<section class="abs hero" role="img" aria-label="Sunny sky over a wide green lawn"></section>
<nav class="abs nav">
  <a class="active" href="#">HOME</a><a href="#">LAWN CARE</a><a href="#">SNOW REMOVAL</a><a href="#">YARD CARE</a><a href="#">CONTACT</a><a href="#">SCHEDULE</a>
</nav>

<div class="abs slide">
  <div class="slide-photo" role="img" aria-label="Photo of two crew members in bright shirts kneeling beside a riding mower in a garage"></div>
  <div class="slide-title">BRISKYARDLLC</div>
  <p class="slide-text">Lorem Ipsum is simply dummy text of the printing and typesetting industry. Lorem Ipsum has been the industry's standard dummy text ever since the 1500s, when an unknown printer took a galley of type and scrambled</p>
  <div class="slide-btn">Read More</div>
</div>
<div class="abs arrow" style="left:29px;top:335px"><svg width="12" height="20"><path d="M10 2 3 10l7 8" stroke="#fff" stroke-width="2" fill="none"/></svg></div>
<div class="abs arrow" style="left:957px;top:335px"><svg width="12" height="20"><path d="M2 2l7 8-7 8" stroke="#fff" stroke-width="2" fill="none"/></svg></div>

<section class="abs features"></section>
<div class="abs feature-box" style="left:100px;top:598px">
  <svg width="34" height="36" viewBox="0 0 34 36"><path d="M3 16h7v18H3zM12 16l6-12c3 0 4 2 3 6l-1 4h9c2 0 3 2 2 4l-3 13c-.5 2-2 3-4 3H12z" fill="none" stroke="#8dc22e" stroke-width="2.6" stroke-linejoin="round"/></svg>
  Best<br>Services
</div>
<div class="abs feature-title" style="left:221px;top:605px">BEST SERVICE</div>
<p class="abs feature-text" style="left:218px;top:630px">Lorem ipsum is simply dummy text of the printing and typesetting industry. Lorem ipsum has been the industry's</p>
<div class="abs feature-box" style="left:519px;top:598px">
  <svg width="40" height="36" viewBox="0 0 40 36"><circle cx="15" cy="18" r="8" fill="none" stroke="#8dc22e" stroke-width="6" stroke-dasharray="4 2.3"/><circle cx="31" cy="8" r="4.5" fill="none" stroke="#8dc22e" stroke-width="4" stroke-dasharray="2.5 1.6"/><circle cx="31" cy="27" r="4.5" fill="none" stroke="#8dc22e" stroke-width="4" stroke-dasharray="2.5 1.6"/></svg>
  Lawn<br>Aeration
</div>
<div class="abs feature-title" style="left:635px;top:605px">LOREM IPSUM AVAILABLE</div>
<p class="abs feature-text" style="left:636px;top:630px">Lorem ipsum is simply dummy text of the printing &amp; typesetting industry. Lorem ipsum has been the industry's</p>

<h2 class="abs section" style="left:94px;top:729px">WELCOME TO BRISKYARDLLC</h2>
<div class="abs welcome-img" role="img" aria-label="Photo of a red push mower cutting green grass"></div>
<p class="abs welcome-text">Brisk Yard, LLC is the vision of Dana Kessler, owner and main grunt. For the last 10 years he has been helping people by cutting their lawn, removing snow, cleaning yards or even just moving firewood, mulch or stones. He felt that it was time to take it to the next level and Brisk Yard, LLC was born. Brisk Yard, LLC is a locally owned business headquartered in Cedar Point, WI. Dana takes personal pride in providing cost effective and timely services to his clients.</p>
<div class="abs read-more">READ MORE &gt;&gt;</div>
<div class="abs cta">Call Brisk Yard, LLC, to get a free estimate 555-014-2200</div>

<h2 class="abs section" style="left:707px;top:728px">QUICK CONTACT</h2>
<div class="abs contact-panel"></div>
<div class="abs field" style="top:773px">NAME</div>
<div class="abs field" style="top:816px">E-MAIL</div>
<div class="abs field" style="top:858px">PHONE</div>
<div class="abs field" style="top:901px;height:48px">QUERY</div>
<div class="abs submit">SUBMIT</div>

<footer class="abs footer"></footer>
<div class="abs footer-links">
  <span>HOME PAGE</span><span class="sep"></span><span>LAWN CARE</span><span class="sep"></span><span>SNOW REMOVAL</span><span class="sep"></span><span>YARD CARE</span><span class="sep"></span><span>CONTACT US</span><span class="sep"></span><span>SCHEDULE</span>
</div>
<div class="abs footer-line"></div>
<div class="abs footer-social"><i></i><i></i><i></i><i></i><i></i></div>
<div class="abs copyright">All rights reserved. © 2014</div>

</body>
</html>
```